Recto Verso Audiology Business Card

Business card with a beautiful design on the back. On the Recto you need the following data Dorvalle Ansel Audiologist Hearing Solutions Hearing Protection Tinnitus Hyperacusis Tel: 0481/27 53 09 Email: On the back, you need something nice like the attached file. The logo "Sola Brisa" can be in the center The colors of the Logo can not be changed If possible stay in the same colors as the logo Another solution is to put the logo on the front and have a nice back (A mosaic of small ears, hearing aids or other ..) Thank you _______________________________________________________________ Visit card On the Recto Dorvalle Ansel Audiologist Hearing Solutions Hearing Protection Tinnitus Hyperacusis Tel: 0481/27 53 09 Email: You can put the logo " Sola Brisa "on the Recto of the Verso The colors of the logo can not be changed. If you put the logo on the back, it must be well integrated. On the Verso I need something in the files. something stylish. It's a visit card for an audiologist. You can get ears of hearing aids if you need. Thanks

Target Market(s)

customers

Contact Information for Business Card

Carte de visite standard ou A6

Font styles to use
Serif
Sans Serif

Colors
33a6d7

Requirements
Must have
• the logo and a stylized background.
Nice to have
• It would be nice to have a back side related to audiology (ears, hearing aids etc.)

```html
<!DOCTYPE html>
<html lang="fr">
<head>
<meta charset="utf-8">
<title>Carte de visite – Dorvalle Ansel, Audiologue</title>
<link rel="stylesheet" href="https://fonts.googleapis.com/css2?family=Open+Sans:wght@300;400&family=Tinos&display=swap">
<style>
  :root {
    --teal: #33a6d7;
    --teal-soft: #52bfd6;
    --ink: #2b3338;
    --paper: #ffffff;
    --backdrop: #e9ecee;
    --photo-dark: #56686d;
    --photo-light: #8a9ca1;
  }
  * { margin: 0; padding: 0; box-sizing: border-box; }
  html, body {
    width: 1200px; height: 1174px; overflow: hidden;
    background: var(--backdrop);
  }
  .sheet {
    position: relative; width: 1200px; height: 1174px;
  }
  .card {
    position: absolute; left: 150px; width: 900px; height: 514px;
    background: var(--paper);
    box-shadow: 0 10px 30px rgba(0,0,0,.15);
    overflow: hidden;
  }
  .card--recto { top: 44px; }
  .card--verso { top: 616px; }
  .card__art { position: absolute; inset: 0; width: 900px; height: 514px; }

  .identity {
    position: absolute; left: 70px; top: 92px;
    font-family: "Open Sans", sans-serif;
  }
  .identity__name {
    font-weight: 300; font-size: 46px; letter-spacing: -0.5px;
    color: var(--teal); text-transform: uppercase; line-height: 1;
  }
  .identity__role {
    font-weight: 400; font-size: 30px; color: var(--ink);
    margin-top: 4px; padding-left: 120px; line-height: 1.1;
  }
  .identity__rule {
    width: 190px; height: 2px; background: var(--teal);
    margin: 26px 0 0 0;
  }
  .services {
    list-style: none; margin-top: 14px; padding-left: 6px;
    font-family: "Tinos", serif; font-size: 21px; color: var(--ink);
    line-height: 1.35;
  }
  .services li:nth-child(2) { padding-left: 16px; }
  .services li:nth-child(3) { padding-left: 32px; }
  .services li:nth-child(4) { padding-left: 46px; }
  .contact {
    display: flex; align-items: center; gap: 10px;
    margin-top: 30px; padding-left: 60px;
    font-family: "Tinos", serif; font-size: 22px; color: var(--ink);
  }
  .contact svg { width: 24px; height: 24px; }

  .brand {
    position: absolute; left: 110px; top: 200px;
    display: flex; align-items: center; gap: 16px;
    font-family: "Open Sans", sans-serif; font-weight: 400;
    font-size: 44px; letter-spacing: 2px; color: var(--teal);
    text-transform: uppercase;
  }
  .brand__square {
    width: 30px; height: 30px; border: 2px solid var(--teal);
  }
</style>
</head>
<body>
<main class="sheet">

  <section class="card card--recto" aria-label="Recto de la carte">
    <svg class="card__art" viewBox="0 0 900 514">
      <defs>
        <linearGradient id="photoTone" x1="0" y1="0" x2="1" y2="1">
          <stop offset="0" stop-color="var(--photo-light)"/>
          <stop offset="1" stop-color="var(--photo-dark)"/>
        </linearGradient>
      </defs>
      <path d="M640,514 C585,420 580,330 640,250 C700,170 650,70 610,0 L900,0 L900,514 Z" fill="var(--teal-soft)"/>
      <path role="img" aria-label="Photo : une main pose un appareil auditif derrière une oreille"
            d="M672,514 C620,420 615,330 672,250 C730,170 688,70 650,0 L900,0 L900,514 Z" fill="url(#photoTone)"/>
      <path d="M612,514 C575,420 570,330 622,250" fill="none" stroke="var(--teal-soft)" stroke-width="4"/>
    </svg>

    <div class="identity">
      <h1 class="identity__name">Dorvalle Ansel</h1>
      <p class="identity__role">Audiologue</p>
      <div class="identity__rule"></div>
      <ul class="services">
        <li>Solutions Auditives</li>
        <li>Protection auditives</li>
        <li>Acouphène</li>
        <li>Hyperacousie</li>
      </ul>
      <p class="contact">
        <svg viewBox="0 0 24 24" aria-hidden="true"><path fill="var(--teal)" d="M6.6 10.8a15.1 15.1 0 0 0 6.6 6.6l2.2-2.2a1 1 0 0 1 1-.25 11.4 11.4 0 0 0 3.6.57 1 1 0 0 1 1 1V20a1 1 0 0 1-1 1A17 17 0 0 1 3 4a1 1 0 0 1 1-1h3.5a1 1 0 0 1 1 1c0 1.25.2 2.45.57 3.57a1 1 0 0 1-.25 1z"/></svg>
        <span>0481/27 53 09</span>
      </p>
    </div>
  </section>

  <section class="card card--verso" aria-label="Verso de la carte">
    <svg class="card__art" viewBox="0 0 900 514" aria-hidden="true">
      <path d="M420,514 C560,470 700,420 760,300 C810,200 830,90 900,30 L900,110 C860,170 840,260 800,340 C740,450 600,500 520,514 Z" fill="var(--teal-soft)"/>
      <path d="M610,470 C720,420 790,330 830,230 C860,150 880,90 900,60" fill="none" stroke="var(--teal-soft)" stroke-width="5"/>
    </svg>
    <div class="brand">
      <span class="brand__square"></span>
      <span>Sola Brisa</span>
    </div>
  </section>

</main>
</body>
</html>
```